Business Card - Design

Create a business card design for my company with graphics on the front and a solid color on the back. The theme for the designs is going to be based on on chinese dragon festivals.

The back of the card will be the simplest as I only want a solid red color with my website address on it: www.lanternbrightnoodles.com

For the front of the card I Want the following on the left side of the card:

Lantern Bright Noodles
Wes Tanbury
(617) 555 - 0148
@lbnharborside

On the right side of the front of the card I want a dragon head either above or "eating" the abbreviation LTBN stacked two letters by two letters. I want all text and graphics to be red on the front of the card with the background being white.

The red used on the back and front of the card must match and be a deep red.
Examples of the red I am looking for, as well as some dragon heads, can be found at the links below:

http://pixelquarry.example/forums/attachments/desktop-skins-orvandel/4471d8830215566-desktop-skins-serpent-saga-orvandel-2.jpg

I like the overall head part of this picture, although the green would be replaced by red. I want a sharp dragon face and teeth/fangs, no whiskers, and no other body parts (arms, feet, etc.). Just the head eating the previously mentioned abbreviation.

```html
<!DOCTYPE html>
<html lang="en">
<head>
<meta charset="utf-8">
<title>Lantern Bright Noodles – Business Card Front</title>
<link rel="stylesheet" href="https://fonts.googleapis.com/css2?family=Source+Sans+3:wght@600&display=swap">
<style>
  :root {
    --deep-red: #e31b2c;
    --card-white: #ffffff;
    --backdrop: #ece9e4;
    --card-shadow: rgba(0, 0, 0, 0.18);
  }
  html, body {
    margin: 0;
    padding: 0;
    width: 1200px;
    height: 900px;
    overflow: hidden;
    background: var(--backdrop);
  }
  .canvas {
    position: relative;
    width: 1200px;
    height: 900px;
    display: flex;
    align-items: center;
    justify-content: center;
  }
  .business-card {
    position: relative;
    width: 1050px;
    height: 600px;
    background: var(--card-white);
    box-shadow: 0 12px 36px var(--card-shadow);
    overflow: hidden;
    font-family: "Source Sans 3", "Myriad Pro", sans-serif;
    font-weight: 600;
    color: var(--deep-red);
  }
  .contact-block {
    position: absolute;
    left: 100px;
    top: 62px;
    font-size: 33px;
    line-height: 1.3;
    letter-spacing: 0.2px;
  }
  .contact-block p { margin: 0; }
  .brand-mark {
    position: absolute;
    right: 78px;
    top: 190px;
    width: 150px;
    display: flex;
    flex-direction: column;
    align-items: center;
    gap: 10px;
  }
  .brand-mark .emblem-disc {
    width: 108px;
    height: 108px;
    border-radius: 50%;
    background: var(--deep-red);
  }
  .brand-mark .initials {
    margin: 0;
    font-size: 50px;
    line-height: 0.95;
    letter-spacing: 4px;
    text-align: center;
    color: var(--deep-red);
  }
  .brand-mark .initials span { display: block; }
  .swoosh {
    position: absolute;
    left: 0;
    top: 0;
    width: 1050px;
    height: 600px;
  }
  .swoosh .band { fill: var(--deep-red); }
  .swoosh .pinstripe { fill: none; stroke: var(--deep-red); stroke-width: 6; }
</style>
</head>
<body>
  <main class="canvas">
    <section class="business-card" aria-label="Lantern Bright Noodles business card, front">
      <div class="contact-block">
        <p class="company-name">Lantern Bright Noodles</p>
        <p class="person-name">Wes Tanbury</p>
        <p class="phone">(617) 555 - 0148</p>
        <p class="social-handle">@lbnharborside</p>
      </div>

      <div class="brand-mark">
        <div class="emblem-disc" role="img" aria-label="Place for the red dragon head emblem above the initials"></div>
        <p class="initials"><span>LT</span><span>BN</span></p>
      </div>

      <svg class="swoosh" viewBox="0 0 1050 600" aria-hidden="true">
        <path class="pinstripe" d="M0,352 C260,360 560,390 1050,505" />
        <path class="band" d="M0,372 C280,382 600,420 1050,535 L1050,560 C650,450 300,420 0,418 Z" />
        <path class="band" d="M0,600 L0,520 C250,470 520,470 760,505 C880,522 980,545 1050,572 L1050,600 Z" />
      </svg>
    </section>
  </main>
</body>
</html>
```